Complete Website Redesign

We need a complete revamp of our website. Need to add interactive custmer catalog seection tools. Need to add customer spec input for recommended product search results. Need a cutomer lead and opportunity contact capability. Need a complete Branding message revamp. Primary visuals will be prodcut pictures and case studies.
Target Market(s)
Industrial Customers in the high durability Air movement and fan/blower space; high durability enclosure and flow industries ie. mining, chamicals, manufacturing, water treatment, chemical in use manufacturing
Look and feel

```html
<!DOCTYPE html>
<html lang="en">
<head>
<meta charset="utf-8">
<title>Duraflow Composites, LLC</title>
<link href="https://fonts.googleapis.com/css2?family=Arimo:wght@400;700&display=swap" rel="stylesheet">
<style>
:root{
  --brand:#1c2f9c;
  --ink:#111;
  --text:#555;
  --muted:#7a7a7a;
  --line:#cfcfcf;
  --panel:#ffffff;
  --page:#f2f2f2;
  --dark:#2e2e2e;
  --footer:#0f0f0f;
  --label-bg:#efefef;
}
*{box-sizing:border-box;margin:0;padding:0}
html,body{width:1200px;height:937px;overflow:hidden}
body{background:var(--page);font-family:"Arimo",Arial,sans-serif;color:var(--text);position:relative}
.sheet{position:absolute;left:120px;top:0;width:960px;height:937px;background:#fff;box-shadow:0 0 12px rgba(0,0,0,.18)}
.abs{position:absolute}
.brand{left:135px;top:40px;display:flex;align-items:center;gap:16px}
.brand-mark{width:40px;height:40px;background:var(--brand)}
.brand-name{font-size:23px;font-weight:700;color:var(--brand);letter-spacing:-.3px}
.request-tab{left:827px;top:71px;width:234px;height:33px;background:var(--brand);border-radius:8px 8px 0 0;color:#fff;font-weight:700;font-size:15px;letter-spacing:.4px;text-align:center;line-height:34px}
.nav{left:318px;top:103px;width:752px;height:38px;border:1px solid var(--line);border-bottom:none;border-radius:4px 4px 0 0;background:linear-gradient(#fdfdfd,#ececec);display:flex;align-items:center;justify-content:space-around;padding:0 6px;font-size:14px;font-weight:700;letter-spacing:.4px;color:#444}
.nav .sep{color:#aaa;font-weight:400}
.nav .current{color:#111}
.hero{left:130px;top:140px;width:940px;height:201px;border:1px solid #bbb;background:#fff;overflow:hidden}
.hero-products{position:absolute;left:18px;top:14px;width:384px;height:112px;background:linear-gradient(135deg,#d8d8d8,#8a8a8a 60%,#c9c9c9)}
.hero-propeller{position:absolute;left:430px;top:0;width:510px;height:201px;background:radial-gradient(ellipse at 72% 70%,#d6d6d6 0,#5a5a5a 30%,#1c1c1c 55%,#fff 78%)}
.hero-title{position:absolute;left:24px;top:136px;width:352px;font-size:31px;font-weight:700;color:var(--ink);letter-spacing:.5px;border-bottom:1px solid #888;line-height:34px}
.hero-sub{position:absolute;left:24px;top:172px;width:354px;text-align:right;font-size:22px;font-weight:700;color:var(--muted);letter-spacing:.5px}
.arrow{position:absolute;top:81px;width:36px;height:36px}
.dots{position:absolute;left:441px;top:187px;display:flex;gap:6px}
.dots span{width:9px;height:9px;border-radius:50%;background:#111;border:1px solid #111}
.dots span.off{background:#fff}
.card{background:var(--panel);box-shadow:0 0 4px rgba(0,0,0,.25)}
.welcome{left:131px;top:357px;width:462px;height:221px;padding:16px 26px 0 18px}
.welcome h2{font-size:17px;color:var(--ink);letter-spacing:.5px;margin-bottom:4px}
.welcome p{font-size:14px;line-height:17px;text-align:justify;color:#555}
.welcome hr{border:none;border-top:1px solid #aaa;margin:16px -14px 14px 0}
.readmore{position:absolute;right:16px;bottom:2px;font-size:12px;font-style:italic;color:var(--brand)}
.label{position:absolute;left:12px;top:10px;width:200px;height:43px;background:var(--label-bg);padding:5px 0 0 8px}
.label b{display:block;font-size:17px;letter-spacing:2.2px;color:#444;line-height:18px}
.label span{display:block;font-size:13px;font-weight:700;letter-spacing:.6px;color:var(--brand);line-height:16px}
.row2 .label{top:13px}
.thumb{position:absolute;left:20px;top:62px;width:184px;height:140px;border:1px solid var(--line);padding:14px}
.row2 .thumb{top:65px}
.thumb div{width:100%;height:100%;background:radial-gradient(circle,#9a9a9a 0,#cfcfcf 45%,#f7f7f7 75%)}
.dark{left:846px;top:357px;width:223px;height:221px;background:var(--dark);padding:16px 18px 0 20px;color:#fff}
.dark b{display:block;font-size:17px;letter-spacing:2.2px;line-height:18px}
.dark .sub{font-size:13px;font-weight:700;letter-spacing:.6px;border-bottom:1px solid #bbb;padding-bottom:4px}
.dark ul{list-style:none;margin-top:6px;border:1px solid #222;padding:4px 0 0 12px;height:140px;background:#2a2a2a}
.dark li{font-size:13px;line-height:22px;display:flex;align-items:center;gap:8px}
.viewall{position:absolute;right:14px;bottom:3px;font-size:11px;font-weight:700;letter-spacing:.5px}
.viewall i{color:#999;font-style:normal}
.address{left:846px;top:592px;width:223px;height:222px;padding:18px 0 0 19px}
.address h3{font-size:17px;letter-spacing:2.2px;color:#444;margin-bottom:26px}
.address strong{display:block;font-size:12px;color:var(--ink)}
.address p{font-size:13px;line-height:20px;color:#555}
.footer{left:131px;top:837px;width:938px;height:77px;background:var(--footer);color:#ccc;font-size:11px}
.footer h4{position:absolute;top:10px;font-size:12px;color:#fff;letter-spacing:.3px}
.footer .col{position:absolute;top:30px;line-height:17px}
.divider{position:absolute;left:592px;top:10px;width:1px;height:58px;background:linear-gradient(transparent,#777,transparent)}
.social{position:absolute;left:716px;top:35px;display:flex;gap:9px}
.social span{width:25px;height:25px;border-radius:3px}
.copyright{left:131px;top:914px;width:938px;height:23px;background:var(--brand);color:#fff;font-size:11px;text-align:center;line-height:23px}
</style>
</head>
<body>
<div class="sheet"></div>

<div class="abs brand"><span class="brand-mark"></span><span class="brand-name">Duraflow Composites, LLC</span></div>
<div class="abs request-tab">REQUEST INFORMATION</div>
<nav class="abs nav">
  <span class="current">HOME</span><span class="sep">|</span><span>PRODUCTS</span><span class="sep">|</span><span>ABOUT US</span><span class="sep">|</span><span>MISSION</span><span class="sep">|</span><span>REQUEST INFORMATION</span><span class="sep">|</span><span>CONTACTS</span>
</nav>

<section class="abs hero">
  <div class="hero-products" role="img" aria-label="Collection of fiberglass fans and blowers"></div>
  <div class="hero-propeller" role="img" aria-label="Close-up of a fiberglass axial propeller"></div>
  <div class="hero-title">FIBERGLASS</div>
  <div class="hero-sub">AXIAL PROPELLERS</div>
  <svg class="arrow" style="left:8px" viewBox="0 0 36 36"><circle cx="18" cy="18" r="16" fill="#fff" stroke="#1d2d4a" stroke-width="3"/><path d="M21 11l-7 7 7 7" fill="none" stroke="#1d2d4a" stroke-width="3.5"/></svg>
  <svg class="arrow" style="left:894px" viewBox="0 0 36 36"><circle cx="18" cy="18" r="16" fill="#fff" stroke="#1d2d4a" stroke-width="3"/><path d="M15 11l7 7-7 7" fill="none" stroke="#1d2d4a" stroke-width="3.5"/></svg>
  <div class="dots"><span></span><span class="off"></span><span></span><span></span></div>
</section>

<section class="abs card welcome">
  <h2>WELCOME</h2>
  <p>We have a wide selection of fiberglass fans and other corrosion resistant air handling solutions for OEM's, Contractors and Plant Maintenance Operations.</p>
  <hr>
  <h2>ABOUT US</h2>
  <p>Here at Duraflow Composites, LLC., we are focused on continu-ous improvement of our operation. Our objective and vision is to capture more market share geographically while serving........</p>
  <span class="readmore">Readmore &gt;&gt;</span>
</section>

<section class="abs card" style="left:607px;top:357px;width:223px;height:221px">
  <div class="label"><b>FIBERGLASS</b><span>AXIAL PROPELLERS</span></div>
  <div class="thumb"><div role="img" aria-label="Fiberglass axial propeller"></div></div>
</section>

<section class="abs dark">
  <b>FIBERGLASS</b>
  <div class="sub">AXIAL FANS</div>
  <ul>
    <li><svg width="13" height="11" viewBox="0 0 13 11"><path d="M0 3.5h7V0l6 5.5-6 5.5V7.5H0z" fill="#fff"/></svg>Lorem Ipsum 1</li>
    <li><svg width="13" height="11" viewBox="0 0 13 11"><path d="M0 3.5h7V0l6 5.5-6 5.5V7.5H0z" fill="#fff"/></svg>Lorem Ipsum 2</li>
    <li><svg width="13" height="11" viewBox="0 0 13 11"><path d="M0 3.5h7V0l6 5.5-6 5.5V7.5H0z" fill="#fff"/></svg>Lorem Ipsum 3</li>
    <li><svg width="13" height="11" viewBox="0 0 13 11"><path d="M0 3.5h7V0l6 5.5-6 5.5V7.5H0z" fill="#fff"/></svg>Lorem Ipsum 4</li>
    <li><svg width="13" height="11" viewBox="0 0 13 11"><path d="M0 3.5h7V0l6 5.5-6 5.5V7.5H0z" fill="#fff"/></svg>Lorem Ipsum 5</li>
    <li><svg width="13" height="11" viewBox="0 0 13 11"><path d="M0 3.5h7V0l6 5.5-6 5.5V7.5H0z" fill="#fff"/></svg>Lorem Ipsum 6</li>
  </ul>
  <span class="viewall">VIEW ALL <i>&gt;&gt;</i></span>
</section>

<section class="abs card row2" style="left:131px;top:592px;width:223px;height:222px">
  <div class="label"><b>FIBERGLASS</b><span>CENTRIFUGAL FANS</span></div>
  <div class="thumb"><div role="img" aria-label="Fiberglass centrifugal fan"></div></div>
</section>
<section class="abs card row2" style="left:370px;top:592px;width:223px;height:222px">
  <div class="label" style="left:11px"><b>FIBERGLASS</b><span>LOUVERS AND DAMPERS</span></div>
  <div class="thumb" style="left:19px"><div role="img" aria-label="Fiberglass damper"></div></div>
</section>
<section class="abs card row2" style="left:607px;top:592px;width:223px;height:222px">
  <div class="label"><b>HIGH PLUME</b><span>EXHAUST FANS</span></div>
  <div class="thumb"><div role="img" aria-label="High plume exhaust fans"></div></div>
</section>

<section class="abs card address">
  <h3>ADDRESS</h3>
  <strong>DURAFLOW COMPOSITES, LLC</strong>
  <p>18 Mill Road / P.O. Box 210<br>Brookfield, NY 14590<br><br>Tel: 555-210-4410<br>Fax: 555-210-4411</p>
</section>

<footer class="abs footer">
  <h4 style="left:29px">ADDRESS</h4>
  <div class="col" style="left:30px">18 Mill Road / P.O. Box 210<br>Brookfield, NY 14590</div>
  <div class="col" style="left:188px">Tel &nbsp;: 555-210-4410<br>Fax : 555-210-4411</div>
  <div class="col" style="left:322px">Email &nbsp;&nbsp;&nbsp;: &nbsp;sales@duraflowcp.com<br>website : &nbsp;www.duraflowcp.com</div>
  <div class="divider"></div>
  <h4 style="left:716px">CONNECT US</h4>
  <div class="social">
    <span style="background:#3b5998"></span>
    <span style="background:#1f6fa3"></span>
    <span style="background:#4fb3e0"></span>
    <span style="background:#d9d9d9"></span>
    <span style="background:#2da62d"></span>
  </div>
</footer>
<div class="abs copyright">Copyright 2012. Duraflow Composites, LLC</div>
</body>
</html>
```